Labels design for a a range of food products

We are looking for labels design for a range of food product. The design should be the same for all the label with brown/black background and gold and white wording like the one attached.
The size and the content of the label will change depending on the different products.
I have also attached the logo to be used which is the logo "CORVANE" Telmora. You shall be using the black and gold version. Brighter/shining gold is better.
The first label to be designed is the one related a plastic tray like the one Cappelletti" file: IMG_20151231_021838
The second label to be designed is the one related to a bottle like the one "Olive Oil" file; IMG_20151231_021651
The third label to be designed is the one related to a jar like the one "Olive Taggiasche" file: IMG_20151231_021531 and IMG_20151231_021549
The fourth label to be designed is the one related to bag like the one IMG_20151231_021506
The fifth label to be designed is the one related to the bottle. IMG_20151231_021426_panorama
This files are only samples. I have attached a file excel "Texts for Labels" in which you will find the text to be applied for the labels.
In order to decide the best design a front and a back label should be provided.

Food Consumers

Product

• Front and Back Label
• Some pictures of the product on the label would be nice to have to recall what is inside.

```html
<!DOCTYPE html>
<html lang="it">
<head>
<meta charset="utf-8">
<title>CORVANE Telmora – Olio extravergine di oliva, etichetta frontale</title>
<link rel="stylesheet" href="https://fonts.googleapis.com/css2?family=Playball&display=swap">
<style>
  :root {
    --stage: #f1f1f1;
    --label-black: #0b0b0b;
    --label-edge: #1c1c1c;
    --swoosh: #5a5a5a;
    --swoosh-soft: #3a3a3a;
    --gold: #c9952e;
    --gold-bright: #e2b54a;
    --white: #ffffff;
    --badge-neutral: #8c8c8c;
  }
  html, body {
    margin: 0;
    padding: 0;
    width: 1200px;
    height: 1200px;
    overflow: hidden;
    background: var(--stage);
  }
  .stage {
    position: relative;
    width: 1200px;
    height: 1200px;
    display: flex;
    align-items: center;
    justify-content: center;
  }
  .front-label {
    display: block;
    width: 330px;
    height: 1120px;
    filter: drop-shadow(0 6px 14px rgba(0,0,0,0.18));
  }
  .script { font-family: "Playball", cursive; }
  .heavy { stroke-width: 0.8; paint-order: stroke; }
</style>
</head>
<body>
<main class="stage">
  <svg class="front-label" viewBox="0 0 330 1120" xmlns="http://www.w3.org/2000/svg" aria-label="Etichetta frontale olio extravergine di oliva">
    <defs>
      <linearGradient id="label-shade" x1="0" y1="0" x2="1" y2="0">
        <stop offset="0" stop-color="#000"/>
        <stop offset="0.5" stop-color="var(--label-edge)"/>
        <stop offset="1" stop-color="#000"/>
      </linearGradient>
      <radialGradient id="sheaf-tone" cx="0.5" cy="0.5" r="0.5">
        <stop offset="0" stop-color="#6a6a6a" stop-opacity="0.85"/>
        <stop offset="1" stop-color="#3a3a3a" stop-opacity="0"/>
      </radialGradient>
      <clipPath id="label-shape">
        <rect width="330" height="1120" rx="22"/>
      </clipPath>
    </defs>

    <g clip-path="url(#label-shape)">
      <rect class="label-ground" width="330" height="1120" fill="url(#label-shade)"/>

      <path class="sweep-arc" d="M330 250 C 120 300, -20 520, 40 820 C 80 980, 220 1060, 330 1080 L330 1000 C 220 970, 120 900, 90 780 C 50 560, 170 370, 330 320 Z" fill="var(--swoosh)"/>
      <path class="sweep-arc-inner" d="M330 600 C 300 680, 300 820, 330 900 Z" fill="var(--swoosh-soft)"/>

      <ellipse class="sheaf-artwork" role="img" aria-label="Spighe di grano decorative in grigio" cx="175" cy="780" rx="150" ry="250" fill="url(#sheaf-tone)"/>

      <path class="base-swoosh" d="M15 1085 C 120 1045, 230 1030, 330 1025 L330 1035 C 230 1040, 120 1058, 15 1085 Z" fill="var(--swoosh)"/>
    </g>

    <g class="brand script" fill="var(--gold-bright)" text-anchor="middle">
      <circle cx="165" cy="128" r="82" fill="none" stroke="var(--gold-bright)" stroke-width="9"/>
      <text x="165" y="240" font-size="34">CORVANE</text>
      <text x="165" y="268" font-size="24">Telmora</text>
    </g>

    <g class="product-title script heavy" fill="var(--white)" stroke="var(--white)" text-anchor="middle">
      <text x="165" y="363" font-size="55">Olio</text>
      <text x="165" y="405" font-size="44">extravergine</text>
      <text x="165" y="443" font-size="44">di oliva</text>
    </g>

    <g class="origin script heavy" fill="var(--gold)" stroke="var(--gold)" text-anchor="middle" font-size="29">
      <text x="165" y="503">Val di Mazara DOP</text>
      <text x="165" y="531">Regione Sicilia</text>
    </g>

    <text class="process script heavy" x="165" y="598" text-anchor="middle" font-size="33" fill="var(--white)" stroke="var(--white)">Estratto a freddo</text>

    <circle class="cert-badge" role="img" aria-label="Marchio di certificazione d'origine" cx="165" cy="791" r="68" fill="var(--badge-neutral)"/>

    <g class="volume">
      <text class="script heavy" x="135" y="1042" text-anchor="middle" font-size="44" fill="var(--white)" stroke="var(--white)">750ml</text>
      <circle cx="232" cy="1030" r="13" fill="none" stroke="var(--white)" stroke-width="4"/>
      <line x1="220" y1="1030" x2="244" y2="1030" stroke="var(--white)" stroke-width="4"/>
    </g>
  </svg>
</main>
</body>
</html>
```